Professional Photography Business cards

I need business cards that include my logo which I have uploaded. I run a photography business. I am open to ideas but I would like one side to have my logo and the other side to have my contact info. I don't have a website made but I do own a website domain. I have uploaded 2 different logo color schemes. My business colors are Blue, black , and white.

Business Name
Business Phone Number
Business Email
Business Website address
Instagram

Industry/Entity Type

Professional Photography

Contact Information for Business Card

Phone Number: 555-314-8027 email: info@tkellan-studios.example Instagram: @t.kellanstudios website doman- www.tkellan-studios.example

Requirements
Must have
• I like the idea of a business card with a full black background front and back of card. My colors must include royal blue, black, and white

```html
<!DOCTYPE html>
<html lang="en">
<head>
<meta charset="utf-8">
<title>T. Kellan Studios – Business Cards</title>
<link href="https://fonts.googleapis.com/css2?family=Arimo:wght@400&display=swap" rel="stylesheet">
<style>
  :root {
    --stage: #2b2b2c;
    --card: #161617;
    --royal-blue: #0f17c9;
    --white: #ffffff;
    --shadow: rgba(0, 0, 0, 0.55);
  }
  * { box-sizing: border-box; margin: 0; padding: 0; }
  html, body {
    width: 1200px;
    height: 866px;
    overflow: hidden;
    background: var(--stage);
    font-family: "Arimo", Arial, sans-serif;
  }
  .stage {
    width: 1200px;
    height: 866px;
    display: flex;
    align-items: center;
    justify-content: center;
    gap: 40px;
  }
  .card {
    position: relative;
    width: 540px;
    height: 309px;
    background: var(--card);
    box-shadow: 6px 10px 18px var(--shadow);
  }
  /* Front: name centred */
  .card--front .brand {
    position: absolute;
    inset: 0;
    display: flex;
    align-items: center;
    justify-content: center;
    gap: 14px;
  }
  .brand__name {
    color: var(--royal-blue);
    font-size: 34px;
    font-weight: 400;
    letter-spacing: 0.04em;
  }
  .brand__dot {
    width: 18px;
    height: 18px;
    border-radius: 50%;
    background: var(--white);
  }
  /* Back: contact details */
  .contact-list {
    position: absolute;
    left: 34px;
    top: 40px;
    list-style: none;
  }
  .contact-list li {
    display: flex;
    align-items: center;
    gap: 10px;
    color: var(--white);
    font-size: 15px;
    line-height: 1;
    margin-bottom: 10px;
  }
  .contact-icon {
    width: 18px;
    height: 18px;
    flex: none;
  }
  .card--back .brand {
    position: absolute;
    right: 34px;
    top: 128px;
    display: flex;
    align-items: center;
    gap: 10px;
  }
  .card--back .brand__name { font-size: 24px; }
  .card--back .brand__dot { width: 13px; height: 13px; }
  .social-handle {
    position: absolute;
    right: 34px;
    bottom: 30px;
    display: flex;
    align-items: center;
    gap: 9px;
    color: var(--white);
    font-size: 16px;
  }
  .social-handle__mark {
    width: 16px;
    height: 16px;
    border-radius: 50%;
    background: var(--royal-blue);
  }
</style>
</head>
<body>
  <main class="stage">
    <section class="card card--front" aria-label="Card front">
      <div class="brand">
        <span class="brand__name">T. Kellan Studios</span>
        <span class="brand__dot"></span>
      </div>
    </section>

    <section class="card card--back" aria-label="Card back">
      <ul class="contact-list">
        <li>
          <svg class="contact-icon" viewBox="0 0 18 18" aria-hidden="true">
            <circle cx="9" cy="9" r="9" fill="var(--royal-blue)"/>
            <path d="M6 4.5l1.8 2.2-1 1.2c.7 1.4 1.6 2.3 3 3l1.2-1 2.2 1.8-1.2 1.6c-3.4-.4-6.4-3.4-6.8-6.8z" fill="var(--card)"/>
          </svg>
          555-314-8027
        </li>
        <li>
          <svg class="contact-icon" viewBox="0 0 18 18" aria-hidden="true">
            <circle cx="9" cy="9" r="9" fill="var(--royal-blue)"/>
            <rect x="4.5" y="6" width="9" height="6.5" fill="none" stroke="var(--card)" stroke-width="1.2"/>
            <path d="M4.5 6l4.5 3.6L13.5 6" fill="none" stroke="var(--card)" stroke-width="1.2"/>
          </svg>
          info@tkellan-studios.example
        </li>
        <li>
          <svg class="contact-icon" viewBox="0 0 18 18" aria-hidden="true">
            <circle cx="9" cy="9" r="9" fill="var(--royal-blue)"/>
            <circle cx="9" cy="9" r="4.6" fill="none" stroke="var(--card)" stroke-width="1.1"/>
            <ellipse cx="9" cy="9" rx="2" ry="4.6" fill="none" stroke="var(--card)" stroke-width="1.1"/>
            <path d="M4.4 9h9.2" stroke="var(--card)" stroke-width="1.1"/>
          </svg>
          www.tkellan-studios.example
        </li>
      </ul>

      <div class="brand">
        <span class="brand__name">T. Kellan Studios</span>
        <span class="brand__dot"></span>
      </div>

      <div class="social-handle">
        @t.kellanstudios
        <span class="social-handle__mark"></span>
      </div>
    </section>
  </main>
</body>
</html>
```